Website for QuillbrookCrew presentation

We need a new website, ideally as a wordpress there, for QuillbrookCrew - we focus on machine learning, big data, data science and data analytics. This website should have two main sections - team presentation, introduction and offered services as static pages, and a blog section.

Target Market(s)

Companies which would like to hire the consultants for data science

Industry/Entity Type

Data Service

Font styles to use
Sans Serif

Colors

Designer to choose colors to be used in the design.

Requirements
Must have
• Wordpress template, blog and presentation pages, nice background images, incorporate the existing logo from brief
Nice to have
• match the word and ppt existing templates for quillbrook crew

```html
<!DOCTYPE html>
<html lang="en">
<head>
<meta charset="utf-8">
<title>QuillbrookCrew — Data Science Consulting</title>
<link href="https://fonts.googleapis.com/css2?family=Poppins:wght@400;500;600;700&family=Open+Sans:wght@400;600&display=swap" rel="stylesheet">
<style>
:root{
  --brand:#3d3b97;
  --brand-deep:#2f2d80;
  --brand-soft:#5553b0;
  --ink:#222230;
  --muted:#8a8a98;
  --line:#e6e6ec;
  --paper:#ffffff;
  --mist:#f5f5f8;
  --night:#1b1b20;
  --night-line:#2c2c33;
  --logo-blue:#2f6fb8;
  --logo-gray:#7d7d85;
}
*{box-sizing:border-box;margin:0;padding:0}
html,body{width:1200px;height:3612px;overflow:hidden}
body{font-family:"Open Sans",Arial,sans-serif;color:var(--ink);background:var(--paper);font-size:11px;line-height:1.6}
h1,h2,h3,h4,.num,.btn,.nav a{font-family:"Poppins",Arial,sans-serif}
.wrap{width:740px;margin:0 auto;position:relative}

/* top bar */
.topbar{height:24px;background:var(--brand);color:#fff;font-size:9px}
.topbar .wrap{display:flex;justify-content:space-between;align-items:center;height:24px}
.topbar .right{display:flex;gap:18px}
.topbar .call{background:var(--brand-deep);padding:0 12px;line-height:24px}

/* nav */
.nav{height:64px;border-bottom:1px solid var(--line)}
.nav .wrap{display:flex;justify-content:flex-end;align-items:center;height:64px;gap:22px}
.nav a{font-size:9px;font-weight:500;color:var(--ink);text-decoration:none;letter-spacing:.5px}
.nav a.active{color:var(--brand)}

/* hero brand */
.hero{height:424px;display:flex;align-items:center;justify-content:center;gap:30px}
.hero .mark{width:120px;height:120px;border-radius:50%;background:var(--logo-blue)}
.hero .name{font-family:"Poppins",Arial,sans-serif;font-weight:700;font-size:96px;line-height:1;color:var(--logo-blue);letter-spacing:-1px}

/* feature cards */
.features{height:288px;background:var(--mist);padding-top:48px}
.features .wrap{display:flex;gap:20px}
.feature{flex:1;background:#fff;border:1px solid var(--line);padding:22px 20px;height:196px}
.feature h3{font-size:12px;font-weight:500;color:var(--brand);text-align:center;margin-bottom:28px}
.feature p{color:var(--muted);font-size:10px}
.feature .more{display:block;margin-top:34px;font-size:8px;font-weight:600;color:var(--ink)}

/* section headings */
.sec-title{font-size:18px;font-weight:500;text-align:center;color:var(--ink)}

/* services */
.services{height:348px;padding-top:30px}
.services .head{display:flex;justify-content:space-between;align-items:center;margin-bottom:22px}
.services .head .sec-title{text-align:left}
.arrows{display:flex;gap:6px}
.arrows span{width:18px;height:18px;border-radius:50%;background:var(--mist);display:flex;align-items:center;justify-content:center}
.svc-row{display:flex;gap:12px}
.svc{flex:1}
.svc .photo{height:160px;position:relative;display:flex;align-items:flex-end;justify-content:center;padding-bottom:8px}
.svc .photo h4{color:#fff;font-size:11px;font-weight:600}
.svc p{color:var(--muted);font-size:9px;margin-top:10px;text-align:center}
.ph-a{background:linear-gradient(160deg,#8a6a55,#3d2f28)}
.ph-b{background:linear-gradient(160deg,#c2a48a,#6a5446)}
.ph-c{background:linear-gradient(160deg,#9aa6b8,#4a4f63)}
.ph-d{background:linear-gradient(160deg,#b28e74,#4f3b32)}

/* stats */
.stats{height:352px;background:var(--brand);color:#fff;padding-top:76px;text-align:center}
.stats h2{font-size:15px;font-weight:500;line-height:1.5;width:440px;margin:0 auto 54px}
.stats .row{display:flex;justify-content:space-between;width:620px;margin:0 auto}
.stat .num{font-size:32px;font-weight:500;line-height:1}
.stat h4{font-size:10px;font-weight:500;margin:10px 0 6px}
.stat p{font-size:8px;opacity:.7;width:120px}

/* projects */
.projects{height:400px;padding-top:10px}
.projects .head{display:flex;justify-content:space-between;align-items:center;margin-bottom:16px}
.projects .head .sec-title{text-align:left}
.btn-outline{font-size:8px;font-weight:600;border:1px solid var(--line);padding:7px 14px;letter-spacing:.5px}
.proj{display:flex;height:320px}
.proj .photo{width:440px;background:linear-gradient(135deg,#b9c3d2,#6f7a90)}
.proj .card{flex:1;background:var(--mist);padding:80px 30px;text-align:center}
.proj .card h3{font-size:13px;font-weight:500}
.proj .card .cat{font-size:8px;color:var(--muted);margin-bottom:12px;display:block}
.proj .card p{font-size:9px;color:var(--muted)}
.proj .card .link{display:block;margin-top:20px;font-size:8px;font-weight:600;color:var(--brand)}

/* news */
.news{height:490px;padding-top:36px}
.news .sec-title{margin-bottom:22px}
.news-row{display:flex;gap:16px}
.post{flex:1}
.post .photo{height:140px}
.post .meta{font-size:8px;color:var(--muted);margin:10px 0 4px}
.post h3{font-size:12px;font-weight:500;line-height:1.35}
.post p{font-size:9px;color:var(--muted);margin-top:8px}
.post .foot{display:flex;justify-content:space-between;margin-top:18px;font-size:8px;color:var(--muted);border-top:1px solid var(--line);padding-top:8px}
.post .foot b{color:var(--ink);font-weight:600}
.n1{background:linear-gradient(140deg,#7b8696,#3a4150)}
.n2{background:linear-gradient(140deg,#9fa7b5,#4d5463)}
.n3{background:linear-gradient(140deg,#aab5c6,#5a6478)}
.dots{display:flex;justify-content:center;gap:6px;margin-top:30px}
.dots i{width:6px;height:6px;border-radius:50%;background:#ccc}
.dots i.on{background:var(--brand)}

/* consultation */
.consult{height:370px;background:linear-gradient(90deg,var(--brand-deep),var(--brand));padding-top:40px;color:#fff}
.consult .wrap{display:flex;justify-content:space-between}
.form{width:460px}
.form h2{font-size:17px;font-weight:500;margin-bottom:20px}
.form .grid{display:grid;grid-template-columns:1fr 1fr;gap:12px}
.field{height:30px;border:1px solid rgba(255,255,255,.35);font-size:8px;padding:8px 10px;color:#fff}
.field.tall{grid-row:span 3;height:auto}
.btn-white{background:#fff;color:var(--brand);font-size:8px;font-weight:600;text-align:center;line-height:30px}
.years{width:220px;height:288px;background:#fff;color:var(--ink);padding:24px 22px;text-align:center}
.years h4{font-size:11px;font-weight:500;line-height:1.4}
.years .num{font-size:40px;color:var(--brand);font-weight:500;margin-top:24px;line-height:1}
.years .lbl{font-size:9px}
.years p{font-size:8px;color:var(--muted);margin-top:22px}

/* feedback */
.feedback{height:320px;padding-top:26px;text-align:center}
.feedback .sec-title{margin-bottom:24px}
.quotes{display:flex;justify-content:center;gap:30px;align-items:flex-start}
.quote{width:200px;color:#c7c7cf;font-size:8px}
.quote.main{width:230px;color:var(--muted);font-size:9px;border:1px solid var(--line);padding:18px}
.avatar{width:34px;height:34px;border-radius:50%;background:linear-gradient(135deg,#b0a090,#6d5e52);margin:16px auto 6px}
.quote h4{font-size:10px;font-weight:500;color:var(--ink)}
.quote .role{font-size:8px}
.quote.side{margin-top:120px}

/* partners */
.partners{height:140px;background:var(--mist);display:flex;align-items:center}
.partners .wrap{display:flex;justify-content:space-between;align-items:center}
.badge{width:74px;height:22px;background:#c9c9d1;border-radius:3px}

/* footer */
.footer{height:392px;background:var(--night);color:#a8a8b2;padding-top:60px;position:relative}
.footer .wrap{display:flex;gap:30px}
.fcol{flex:1}
.fcol h4{color:#fff;font-size:11px;font-weight:500;margin-bottom:14px}
.fcol p,.fcol li{font-size:8px;list-style:none;margin-bottom:7px}
.fbrand{display:flex;align-items:center;gap:8px;margin-bottom:14px}
.fbrand i{width:16px;height:16px;border-radius:50%;background:var(--brand-soft)}
.fbrand span{font-family:"Poppins",Arial,sans-serif;color:#fff;font-size:14px;font-weight:600}
.fbtn{display:inline-block;border:1px solid var(--night-line);color:#fff;font-size:8px;padding:7px 14px;margin-top:8px}
.fpost b{display:block;color:#fff;font-size:8px;font-weight:600}
.fpost span{font-size:7px}
.contact li{display:flex;align-items:center;gap:8px}
.contact li em{width:14px;height:14px;border-radius:50%;background:var(--night-line);display:inline-block}
.socials{display:flex;gap:10px;margin-top:10px}
.socials i{width:8px;height:8px;background:#6a6a74}
.copy{position:absolute;left:0;right:0;bottom:0;height:40px;border-top:1px solid var(--night-line);font-size:8px}
.copy .wrap{display:flex;justify-content:space-between;align-items:center;height:40px}
.copy .links{display:flex;gap:16px}
</style>
</head>
<body>

<div class="topbar"><div class="wrap">
  <span>Data-driven consulting for growing teams</span>
  <div class="right"><span>Mon–Fri 9:00</span><span>Office</span><span class="call">Call: 555 0142 889</span></div>
</div></div>

<nav class="nav"><div class="wrap">
  <a class="active">HOME</a><a>ABOUT US</a><a>SERVICES</a><a>PROJECTS</a><a>BLOG</a><a>SHOP</a><a>CONTACT</a>
  <svg width="10" height="10" viewBox="0 0 10 10"><circle cx="4" cy="4" r="3" fill="none" stroke="#222230" stroke-width="1.2"/><line x1="6.3" y1="6.3" x2="9" y2="9" stroke="#222230" stroke-width="1.2"/></svg>
</div></nav>

<header class="hero">
  <span class="mark"></span>
  <span class="name">QUILLBROOK<br>CREW</span>
</header>

<section class="features"><div class="wrap">
  <article class="feature"><h3>Professional</h3><p>Our analysts turn raw records into clear models, reliable forecasts and reports your team can act on every week.</p><span class="more">READ MORE</span></article>
  <article class="feature"><h3>Professional</h3><p>We build data pipelines that scale with your business and keep every dashboard fresh, accurate and easy to trust.</p><span class="more">READ MORE</span></article>
  <article class="feature"><h3>Professional</h3><p>From first audit to live machine learning, our consultants guide each step and hand over clear, documented work.</p><span class="more">READ MORE</span></article>
</div></section>

<section class="services"><div class="wrap">
  <div class="head"><h2 class="sec-title">Our Main Services</h2>
    <div class="arrows">
      <span><svg width="6" height="8" viewBox="0 0 6 8"><path d="M5 1L2 4l3 3" fill="none" stroke="#222230" stroke-width="1.2"/></svg></span>
      <span><svg width="6" height="8" viewBox="0 0 6 8"><path d="M1 1l3 3-3 3" fill="none" stroke="#222230" stroke-width="1.2"/></svg></span>
    </div></div>
  <div class="svc-row">
    <div class="svc"><div class="photo ph-a" role="img" aria-label="Photo of a consultant at work"><h4>Business Growth</h4></div><p>Models that reveal where your next revenue comes from.</p></div>
    <div class="svc"><div class="photo ph-b" role="img" aria-label="Photo of a team meeting"><h4>Sustainability</h4></div><p>Long-term data strategy built around your goals.</p></div>
    <div class="svc"><div class="photo ph-c" role="img" aria-label="Photo of a colleague reviewing results"><h4>Performance</h4></div><p>Faster queries and leaner pipelines for every team.</p></div>
    <div class="svc"><div class="photo ph-d" role="img" aria-label="Photo of a smiling analyst"><h4>Customer Insights</h4></div><p>Know your clients through clean, joined-up data.</p></div>
  </div>
</div></section>

<section class="stats">
  <h2>There is some reason behind why people choose QuillbrookCrew past 20 years for their business solutions.</h2>
  <div class="row">
    <div class="stat"><div class="num">376</div><h4>Years Of Experience</h4><p>Combined years our team has spent on data work.</p></div>
    <div class="stat"><div class="num">145</div><h4>Best Consultants</h4><p>Experts in statistics, modelling and engineering.</p></div>
    <div class="stat"><div class="num">92</div><h4>Awards Winning</h4><p>Recognition for projects that made a real impact.</p></div>
    <div class="stat"><div class="num">289</div><h4>Happy Clients</h4><p>Companies that trust us with their data every day.</p></div>
  </div>
</section>

<section class="projects"><div class="wrap">
  <div class="head"><h2 class="sec-title">Latest Projects</h2><span class="btn-outline">VIEW ALL PROJECTS</span></div>
  <div class="proj">
    <div class="photo" role="img" aria-label="Photo of a team working together on laptops"></div>
    <div class="card"><h3>Consumer Products</h3><span class="cat">Business Growth</span><p>A demand forecasting model that cut stock waste and helped a retail client plan every season with confidence.</p><span class="link">READ MORE</span></div>
  </div>
</div></section>

<section class="news"><div class="wrap">
  <h2 class="sec-title">Our Latest News</h2>
  <div class="news-row">
    <article class="post"><div class="photo n1" role="img" aria-label="Photo of a business meeting"></div><div class="meta">By Admin &nbsp; January 14, 2024</div><h3>A digital prescription for the pharma industry</h3><p>How clean clinical data and smart models shorten research cycles.</p><div class="foot"><b>READ MORE</b><span>0 Comments</span></div></article>
    <article class="post"><div class="photo n2" role="img" aria-label="Photo of colleagues at a desk"></div><div class="meta">By Admin &nbsp; January 14, 2024</div><h3>Why buying a big house is a bad investment</h3><p>What the numbers really say about property and long-term value.</p><div class="foot"><b>READ MORE</b><span>0 Comments</span></div></article>
    <article class="post"><div class="photo n3" role="img" aria-label="Photo of a group discussion"></div><div class="meta">By Admin &nbsp; January 14, 2024</div><h3>Successful business tips in 2024 only to grow</h3><p>Simple data habits that help small teams make better calls.</p><div class="foot"><b>READ MORE</b><span>0 Comments</span></div></article>
  </div>
  <div class="dots"><i class="on"></i><i></i></div>
</div></section>

<section class="consult"><div class="wrap">
  <div class="form">
    <h2>Get a Free Consultation</h2>
    <div class="grid">
      <div class="field">Your Name</div>
      <div class="field tall">Tell us about your data project...</div>
      <div class="field">Your Email</div>
      <div class="field">Phone Number</div>
      <div></div>
      <div class="btn-white">SUBMIT NOW</div>
    </div>
  </div>
  <aside class="years">
    <h4>Since 2004, we provide best service for our clients.</h4>
    <div class="num">26</div><div class="lbl">Years of experience</div>
    <p>Our consultants help teams of every size turn data into decisions that last.</p>
  </aside>
</div></section>

<section class="feedback"><div class="wrap">
  <h2 class="sec-title">Customer Feedback</h2>
  <div class="quotes">
    <div class="quote side"><h4 style="color:#c7c7cf">Client Name</h4><span class="role">Manager</span></div>
    <div class="quote main">
      <p>QuillbrookCrew rebuilt our reporting from the ground up. We now see results the same day and plan with real numbers.</p>
      <div class="avatar" role="img" aria-label="Client portrait"></div>
      <h4>Corin Waldley</h4><span class="role">Operations Lead</span>
    </div>
    <div class="quote side"><h4 style="color:#c7c7cf">Client Name</h4><span class="role">Director</span></div>
  </div>
</div></section>

<section class="partners"><div class="wrap">
  <span class="badge"></span><span class="badge"></span><span class="badge"></span><span class="badge"></span><span class="badge"></span><span class="badge"></span>
</div></section>

<footer class="footer">
  <div class="wrap">
    <div class="fcol">
      <div class="fbrand"><i></i><span>QuillbrookCrew</span></div>
      <p>We help companies collect, clean and model their data, then turn it into clear answers.</p>
      <span class="fbtn">Read More</span>
    </div>
    <div class="fcol"><h4>Useful Links</h4><ul><li>About Us</li><li>Services</li><li>Projects</li><li>Blog</li><li>Contact</li><li>Team Members</li></ul></div>
    <div class="fcol"><h4>Latest News</h4>
      <div class="fpost"><b>Successful business tips in 2024</b><span>January 14, 2024</span></div><br>
      <div class="fpost"><b>Why buying a big house</b><span>January 14, 2024</span></div><br>
      <div class="fpost"><b>A digital prescription for pharma</b><span>January 14, 2024</span></div>
    </div>
    <div class="fcol contact"><h4>Contact Details</h4><ul>
      <li><em></em>48 Harrow Lane, Fenwick</li>
      <li><em></em>555 0142 889</li>
      <li><em></em>hello@quillbrookcrew.test</li></ul>
      <div class="socials"><i></i><i></i><i></i><i></i></div>
    </div>
  </div>
  <div class="copy"><div class="wrap">
    <span>Copyright © 2024 QuillbrookCrew. All rights reserved.</span>
    <div class="links"><span>Home</span><span>About</span><span>Services</span><span>Blog</span><span>Contact</span></div>
  </div></div>
</footer>

</body>
</html>
```